Spaces That Serve - Invitation

Need a three fold, 8.5 X 11 invitation that will be direct mail for a seminar. We develop properties for churches in the United States. Final design should communicate a compelling reason for church leaders to attend the "Spaces That Serve" seminar. To be clear, the folded and complete invitation is 8.5" X 11" so there are a total of 6 panels measuring 8.5" X 11". Thanks and have fun.
Updates

Went on vacation/holiday

Target Market(s)

Young start up churches, highly energetic, not traditional at all.

Colors
0054AA
0677BA
7BADD7
CADEEF
E8F1F8
FFF300
FFF600
FEFA6F
FFFEC7
FFFEE8
FFC000
F8CF3A
FAE287
FDF2CF
FEFAEE
EB3D1F
EC4F4E
F09395
F8D3D4
FCEDEE

Requirements
Must have
• See the mock up brochure that I made up. It has all the info I need.
Nice to have
• Open space. Mock up is much too busy looking. Gives me a headache!
Should not have
• Nothing traditional church looking.

```html
<!DOCTYPE html>
<html lang="en">
<head>
<meta charset="utf-8">
<title>Spaces That Serve – Seminar Invitation</title>
<link rel="stylesheet" href="https://fonts.googleapis.com/css2?family=Bitter:wght@400;600;700&family=Roboto:wght@300;400;500&display=swap">
<style>
:root{
  --page:#d5d6d9;
  --slate:#474b5e;
  --slate-deep:#3f4355;
  --slate-soft:#4d5166;
  --slate-band:#53576c;
  --gold:#f4b41a;
  --ink:#2f3342;
  --paper:#ffffff;
  --mist:#f6f6f7;
  --text-light:#eef0f4;
}
*{box-sizing:border-box;margin:0;padding:0}
html,body{width:779px;height:1200px;overflow:hidden;background:var(--page)}
body{position:relative;font-family:"Roboto",Arial,sans-serif;font-weight:300;color:var(--ink)}
.spread{position:absolute;left:64px;width:644px;height:497px;overflow:hidden}
.spread--outside{top:76px;background:var(--slate)}
.spread--inside{top:616px;background:var(--paper)}
.block{position:absolute}
.photo{position:absolute}
.serif{font-family:"Bitter",Georgia,serif}
.body-copy{font-size:7.9px;line-height:11.6px;color:var(--text-light)}
.justify{text-align:justify}

/* outside: story panel */
.story{left:0;top:0;width:215px;height:497px;background:var(--slate-deep)}
.story p{position:absolute;left:11px;width:255px}
.story .intro{top:10px;width:190px}
.story .intro p{position:static;width:auto;margin-bottom:11px}
.story .news{top:309px;left:11px;width:192px}
.story .quote{top:441px;left:12px;font-size:8.6px;line-height:12px;font-weight:400;color:#fff}
.story .verse{top:474px;left:12px;font-size:8.6px;font-weight:400;color:#fff}
.photo--campus{left:0;top:156px;width:210px;height:146px;background:linear-gradient(180deg,#b9d3ec 0%,#dfe8ef 35%,#c9b79c 55%,#7f9a55 80%,#6e8a47 100%)}
.photo--couple{left:131px;top:136px;width:62px;height:62px;border-radius:50%;background:radial-gradient(circle at 50% 40%,#e9e2d8,#8a6a55 75%);border:1.5px solid #fff}

/* outside: topics panel */
.topics{left:215px;top:0;width:217px;height:497px;background:var(--slate-soft)}
.topics .band{position:absolute;left:0;top:0;width:217px;height:30px;background:var(--slate-deep)}
.topics h2{position:absolute;left:13px;top:9px;font-size:10.6px;font-weight:400;color:#fff;letter-spacing:-.1px}
.help-list{position:absolute;left:13px;top:35px;width:190px;list-style:none}
.help-list li{position:relative;padding-left:10px;font-size:7.6px;line-height:9.6px;color:var(--text-light);margin-bottom:5.8px}
.help-list li::before{content:"";position:absolute;left:0;top:3px;width:3px;height:3px;border-radius:50%;background:#fff}
.topics h3{position:absolute;left:14px;top:143px;width:180px;font-size:10.4px;line-height:13.5px;font-weight:400;color:#fff}
.topic-list{position:absolute;left:14px;top:179px;list-style:none}
.topic-list li{position:relative;padding-left:10px;font-size:7.1px;line-height:10.72px;color:var(--text-light)}
.topic-list li::before{content:"";position:absolute;left:1px;top:3px;border-left:3px solid #fff;border-top:2px solid transparent;border-bottom:2px solid transparent}
.photo--lodge{left:0;top:312px;width:217px;height:86px;background:linear-gradient(180deg,#5f6478 0%,#8d98a6 30%,#b28e68 60%,#6b6a55 100%);clip-path:polygon(0 0,100% 0,100% 77%,0 100%)}
.mailer{position:absolute;left:0;top:378px;width:217px;height:119px;background:var(--paper);clip-path:polygon(0 20%,100% 0,100% 100%,0 100%)}
.brand-small{position:absolute;left:0;width:217px;top:405px;text-align:center;font-family:"Bitter",Georgia,serif;font-weight:400;font-size:13px;color:#4a4e60;letter-spacing:.4px}
.address{position:absolute;left:0;width:217px;top:449px;text-align:center;font-family:"Bitter",Georgia,serif;font-size:9.4px;line-height:15px;color:var(--ink)}

/* outside: cover panel */
.cover{left:431px;top:0;width:213px;height:497px;background:var(--slate)}
.cover .center{position:absolute;left:0;width:213px;text-align:center}
.cover-top{position:absolute;left:0;top:0;width:213px;height:185px;background:var(--slate-deep)}
.kicker{top:10px;font-family:"Bitter",Georgia,serif;font-weight:700;font-size:19px;color:var(--gold)}
.lead{top:35px;font-family:"Bitter",Georgia,serif;font-size:12px;color:#fff}
.seminar{top:60px;font-family:"Bitter",Georgia,serif;font-weight:600;font-size:13.4px;line-height:15.4px;color:var(--gold)}
.learn{top:97px;font-size:7.7px;line-height:11.5px;font-weight:400;color:#fff}
.dates{top:143px;font-family:"Bitter",Georgia,serif;font-size:11.3px;color:#fff}
.cities{top:162px;font-size:7.9px;font-weight:400;color:var(--text-light)}
.price{top:194px;font-family:"Bitter",Georgia,serif;font-weight:500;font-size:14px;line-height:17px;color:var(--gold)}
.photo--speaker-badge{left:28px;top:240px;width:44px;height:44px;border-radius:50%;background:radial-gradient(circle at 50% 40%,#d7c7b6,#5b6a7c 75%)}
.speaker-tag{position:absolute;left:88px;top:241px;font-size:10.4px;line-height:14.6px;color:#fff}
.speaker-tag strong{font-weight:500}
.contact-band{position:absolute;left:0;top:298px;width:213px;height:47px;background:var(--slate-band)}
.contact{top:307px;font-size:9.6px;line-height:15px;font-weight:300;color:#fff}
.web-band{position:absolute;left:0;top:348px;width:213px;height:22px;background:var(--slate-band)}
.web{top:353px;font-size:9.6px;font-weight:300;color:#fff}
.brand-large{top:377px;font-family:"Bitter",Georgia,serif;font-weight:400;font-size:17px;line-height:19px;color:#f2f3f6;letter-spacing:.5px}
.photo--office{left:0;top:415px;width:213px;height:82px;background:linear-gradient(180deg,#59607a 0%,#a9b8cc 35%,#c6a78a 62%,#4e6a3a 85%,#6a6f72 100%)}

/* inside spread */
.panel-white{background:var(--paper)}
.inside-h{font-family:"Bitter",Georgia,serif;font-weight:700;color:var(--slate-deep);letter-spacing:-.2px}
.inside-p{font-size:8.9px;line-height:13.6px;font-weight:300;color:var(--ink)}
.feel{left:0;top:0;width:215px;height:105px}
.feel h2{position:absolute;left:19px;top:13px;font-size:12px}
.feel .inside-p{position:absolute;left:19px;top:34px;width:185px}
.feel .inside-p p{margin-bottom:6px}
.photo--prairie{left:0;top:105px;width:215px;height:110px;background:linear-gradient(180deg,#6d98cb 0%,#b8cde4 40%,#d9cdb5 62%,#9aa2a6 78%,#6f8d45 100%)}
.ask h2{position:absolute;left:19px;top:226px;width:180px;font-size:12px;line-height:17px}
.ask .inside-p{position:absolute;left:18px;top:260px;width:180px}
.photo--hope{left:0;top:330px;width:215px;height:89px;background:linear-gradient(180deg,#5f84b4 0%,#b0c4db 30%,#c9b38f 60%,#7c9a54 100%)}
.come h2{position:absolute;left:19px;top:428px;font-size:12px}
.come .inside-p{position:absolute;left:19px;top:446px;width:165px}

.about{left:215px;top:0;width:429px;height:128px;background:var(--slate-deep)}
.about h2{position:absolute;left:15px;top:11px;font-family:"Bitter",Georgia,serif;font-weight:700;font-size:11.6px;color:#fff}
.about p{position:absolute;left:15px;top:35px;width:280px;font-size:7.9px;line-height:11.3px;color:var(--text-light)}
.photo--portrait{left:318px;top:12px;width:104px;height:116px;background:linear-gradient(180deg,#4a4e62 0%,#5c6070 25%,#2a2f45 60%,#242a40 100%);border-radius:44px 44px 0 0}
.photo--crossroads{left:215px;top:128px;width:216px;height:201px;background:linear-gradient(180deg,#8fa98f 0%,#c6b9a0 30%,#b79d7a 55%,#8a6d50 80%,#9b9994 100%)}
.maximize{left:431px;top:128px;width:213px;height:201px}
.maximize h2{position:absolute;left:17px;top:9px;width:195px;font-size:12px;line-height:17.5px}
.maximize .intro{position:absolute;left:16px;top:49px;width:190px}
.maximize h3{position:absolute;left:17px;top:101px;font-size:12px}
.maximize .who{position:absolute;left:16px;top:118px;width:192px}
.maximize .invite{position:absolute;left:17px;top:170px;font-family:"Bitter",Georgia,serif;font-weight:600;font-size:9.2px;line-height:14px;color:var(--slate-deep)}
.learn-box{left:215px;top:329px;width:216px;height:168px;background:var(--mist)}
.learn-box h2{position:absolute;left:21px;top:12px;width:160px;font-size:12px;line-height:17.5px}
.learn-box .inside-p{position:absolute;left:20px;top:53px;width:185px}
.photo--lodge-wide{left:431px;top:329px;width:213px;height:168px;background:linear-gradient(180deg,#557fb3 0%,#9fbbd8 28%,#b79370 50%,#6e5e4c 68%,#3f4044 88%,#55575b 100%)}
</style>
</head>
<body>

<section class="spread spread--outside" aria-label="Outside of invitation">
  <div class="block story">
    <div class="block intro body-copy justify">
      <p>I remember sitting at my desk back in 2001, wondering what am I going to do? Wishing that there was someone I could call that had the knowledge and experience to guide me in the right direction. That is when a seminar invitation showed up on my desk and I soon met Dan Whitmore.</p>
      <p>Since then, Cedar Grove Fellowship has gone through numerous building programs, grown to over 5,000 in attendance and grown into a thriving ministry with a high global impact.</p>
    </div>
    <div class="photo photo--campus" role="img" aria-label="Photo of a church campus with a playground"></div>
    <div class="photo photo--couple" role="img" aria-label="Round portrait of a pastor couple"></div>
    <p class="news body-copy justify">Here’s the bad news: The average tenure of a pastor after a significant building project is twenty-two months. Over half of the churches in the U.S. have a set of plans (stuck behind the pastor’s door) that will never be built. To top it off, construction is the second most litigated industry in the U.S., behind medical. Some pastors will deal with these statistics by never building. Some will forge ahead alone and often become one of these statistics. The good news is that others will seek out those who have built to gain counsel and wisdom.</p>
    <p class="quote">“Plans fail for lack of counsel, but with many advisors they succeed”</p>
    <p class="verse">– Proverbs 15:22</p>
  </div>

  <div class="block topics">
    <div class="band"></div>
    <h2 class="serif">We help Pastors and church leaders to:</h2>
    <ul class="help-list">
      <li>Develop state-of-the-art facilities that are functional &amp; affordable</li>
      <li>Reduce the stress and distractions of a building program</li>
      <li>Avoid the pitfalls of typical building projects</li>
      <li>Eliminate those unexpected surprises</li>
      <li>Maximize Ministry Momentum by eliminating growth barriers.</li>
    </ul>
    <h3 class="serif">The seminar teaches a variety of topics including:</h3>
    <ul class="topic-list">
      <li>10-Steps to Your New Facility</li>
      <li>Creative Land Acquisition</li>
      <li>Funding Your Building Program</li>
      <li>What Type of Building is Right for You</li>
      <li>Creative Church Designs</li>
      <li>Time and Talent Surveys</li>
      <li>Meet Your Development Team</li>
      <li>Debt-Free Development</li>
      <li>Understanding the Permit Process</li>
      <li>Dealing with Nasty Neighbors</li>
      <li>Developing a Communication Plan</li>
      <li>Master Planning Your Campus</li>
    </ul>
    <div class="photo photo--lodge" role="img" aria-label="Photo of a lodge-style church building"></div>
    <div class="mailer"></div>
    <p class="brand-small">Whitmore Facility Solutions</p>
    <p class="address">4720 Quiet Meadow Lane,<br>Larkspur, Colorado 80118</p>
  </div>

  <div class="block cover">
    <div class="cover-top"></div>
    <p class="center kicker">PASTOR!</p>
    <p class="center lead">Lead your church with confidence.</p>
    <p class="center seminar">Attend the Spaces That Serve<br>Seminar</p>
    <p class="center learn">Learn how to DESIGN, FINANCE and BUILD the<br>most creative, functional, and affordable<br>church facilities in America!</p>
    <p class="center dates">Coming to the Bay Area, March 4 - 7</p>
    <p class="center cities">Santa Rosa | Walnut Creek | San Jose | San Mateo</p>
    <p class="center price">Seminar cost is just<br>$29 and includes lunch!</p>
    <div class="photo photo--speaker-badge" role="img" aria-label="Round portrait of the speaker"></div>
    <p class="speaker-tag"><strong>Daniel R. Whitmore</strong><br>America’s #1<br>Church Developer</p>
    <div class="contact-band"></div>
    <p class="center contact">Contact Dan Whitmore to register.<br>Seating is limited!</p>
    <div class="web-band"></div>
    <p class="center web">DanWhitmore.com | dan@whitmorebuilds.com</p>
    <p class="center brand-large">Whitmore<br>Facility Solutions</p>
    <div class="photo photo--office" role="img" aria-label="Photo of a modern church office building with palm trees"></div>
  </div>
</section>

<section class="spread spread--inside" aria-label="Inside of invitation">
  <div class="block feel panel-white">
    <h2 class="inside-h">Feeling a bit overwhelmed?</h2>
    <div class="inside-p">
      <p>We get it. God is growing your ministry, but your current facilities cannot sustain it.</p>
      <p>Where do you start? Who do you call? What are you going to do?</p>
    </div>
  </div>
  <div class="photo photo--prairie" role="img" aria-label="Photo of a modern church building with a cross"></div>
  <div class="ask">
    <h2 class="inside-h">Asking God for guidance and direction?</h2>
    <p class="inside-p">You need a Kingdom-focused ally with over forty years’ experience developing hundreds of state-of-the-art Christian church facilities all across America.</p>
  </div>
  <div class="photo photo--hope" role="img" aria-label="Photo of a stucco church building with a cross on the roof"></div>
  <div class="come">
    <h2 class="inside-h">That is where we come in!</h2>
    <p class="inside-p">Discover the possibilities you may not even know exist and then seize your God-given potential!</p>
  </div>

  <div class="block about">
    <h2>About our speaker</h2>
    <p class="justify">Dan Whitmore, founder of Whitmore Facility Solutions, is America’s top developer of Christian church facilities. Beginning in 1980, Dan has used his wisdom and experience to help ministries like yours overcome the challenges to their facility needs and growth barriers. Dan’s unique understanding of ministry needs makes him a trusted partner for churches that need functional and affordable facilities that are designed to grow with them.</p>
    <div class="photo photo--portrait" role="img" aria-label="Portrait of the speaker in a dark shirt"></div>
  </div>
  <div class="photo photo--crossroads" role="img" aria-label="Photo of a stone church entrance with a green roof"></div>
  <div class="block maximize panel-white">
    <h2 class="inside-h">Maximize your ministry potential for greater Kingdom impact!</h2>
    <p class="inside-p intro">Cast a clear and compelling vision for the future and build a road map connecting your current reality to your future potential!</p>
    <h3 class="inside-h">Who should attend?</h3>
    <p class="inside-p who">Whether you are looking to relocate, expand, remodel, or build new, this seminar will equip you with the tools and confidence you need.</p>
    <p class="invite">Pastors, elders, church staff,<br>and volunteers are all invited!</p>
  </div>
  <div class="block learn-box">
    <h2 class="inside-h">Learn from the experience of others!</h2>
    <p class="inside-p">If you are looking for expert guidance and direction in the design, finance, and construction of your new, expanded, or remodeled facilities, then this is your opportunity to learn from the nation’s leading expert on church design, finance, and construction.</p>
  </div>
  <div class="photo photo--lodge-wide" role="img" aria-label="Photo of a lodge-style church building and parking lot"></div>
</section>

</body>
</html>
```